Nutracuetical supplement label

Will be private labeling a variety of nutraceutical supplements for a holistic health and weight loss clinics. We have a trademarked logo and colors of green and blue. The green is: Pantone 376 c56 y100. The blue is: Pantone 301 C: 100% M: 40% Y: 0% K: 40%.
The look should be fresh with a smacking of clinical rather than earthy. Lots of white space without looking bland. Please use both our colors and refer to our website for other ideas VentolaCare.com.
Updates
Project Deadline Extended
Reason: Lots of good designs. I will be asking each of the (3) finalists for a minor change and make a final decision on Oct 20th. Thank you for your designs and creativity.
Target Market(s)
Weight loss patients investing in clinically proven program.
Industry/Entity Type
Health
Look and feel
Each slider illustrates characteristics of the customer's brand and the style your logo design should communicate.

```html
<!DOCTYPE html>
<html lang="en">
<head>
<meta charset="utf-8">
<title>Ventola Care – Supplement Hang Tags</title>
<link rel="stylesheet" href="https://fonts.googleapis.com/css2?family=Arimo:ital,wght@0,400;1,400&display=swap">
<style>
  :root {
    --brand-green: #7ac143;
    --brand-blue: #005289;
    --ink-blue: #0f5c9c;
    --tag-white: #ffffff;
    --hole: #eeeeee;
    --backdrop: #ececec;
  }
  html, body {
    margin: 0;
    padding: 0;
    width: 1200px;
    height: 1000px;
    overflow: hidden;
    background: var(--backdrop);
  }
  .label-sheet {
    display: block;
    width: 1200px;
    height: 1000px;
    font-family: "Arimo", Arial, sans-serif;
  }
  .tag-head { fill: var(--tag-white); }
  .tag-hole { fill: var(--hole); }
  .tag--green .tag-body { fill: var(--brand-green); }
  .tag--blue .tag-body { fill: var(--brand-blue); }
  .brand-mark { fill: var(--brand-blue); }
  .brand-name { fill: var(--brand-blue); font-size: 34px; letter-spacing: 1px; }
  .brand-tagline { fill: var(--brand-blue); font-size: 9px; }
  .product-name { font-size: 40px; }
  .product-descriptor { font-size: 25px; }
  .product-count { font-size: 24px; }
  .product-notice { font-size: 17px; font-style: italic; }
  .tag--green .product-name,
  .tag--green .product-descriptor,
  .tag--green .product-count,
  .tag--green .product-notice { fill: var(--ink-blue); }
  .tag--blue .product-name { fill: var(--brand-green); }
  .tag--blue .product-descriptor,
  .tag--blue .product-count,
  .tag--blue .product-notice { fill: var(--tag-white); }
</style>
</head>
<body>
<svg class="label-sheet" viewBox="0 0 1200 1000" xmlns="http://www.w3.org/2000/svg">
  <defs>
    <clipPath id="tag-shape">
      <rect x="0" y="0" width="378" height="387" rx="18" ry="18"/>
    </clipPath>
  </defs>

  <!-- Green variant -->
  <g class="tag tag--green" transform="translate(139 323)">
    <g clip-path="url(#tag-shape)">
      <rect class="tag-body" x="0" y="0" width="378" height="387"/>
      <path class="tag-head" d="M0 0 H378 V57 Q189 230 0 57 Z"/>
    </g>
    <circle class="tag-hole" cx="69" cy="37" r="17"/>
    <circle class="brand-mark" cx="112" cy="51" r="8"/>
    <text class="brand-name" x="128" y="63">Ventola Care</text>
    <text class="brand-tagline" x="189" y="120" text-anchor="middle">Maximize Your Weight Health Journey</text>
    <text class="product-name" x="189" y="230" text-anchor="middle">PRODUCT NAME</text>
    <text class="product-descriptor" x="189" y="257" text-anchor="middle">descriptor words</text>
    <text class="product-count" x="189" y="303" text-anchor="middle">50 capsules</text>
    <text class="product-notice" x="189" y="349" text-anchor="middle">Dietary supplement</text>
    <text class="product-notice" x="189" y="371" text-anchor="middle">or professional use only</text>
  </g>

  <!-- Blue variant -->
  <g class="tag tag--blue" transform="translate(691 323)">
    <g clip-path="url(#tag-shape)">
      <rect class="tag-body" x="0" y="0" width="378" height="387"/>
      <path class="tag-head" d="M0 0 H378 V57 Q189 230 0 57 Z"/>
    </g>
    <circle class="tag-hole" cx="69" cy="37" r="17"/>
    <circle class="brand-mark" cx="112" cy="51" r="8"/>
    <text class="brand-name" x="128" y="63">Ventola Care</text>
    <text class="brand-tagline" x="189" y="120" text-anchor="middle">Maximize Your Weight Health Journey</text>
    <text class="product-name" x="189" y="230" text-anchor="middle">PRODUCT NAME</text>
    <text class="product-descriptor" x="189" y="257" text-anchor="middle">descriptor words</text>
    <text class="product-count" x="189" y="303" text-anchor="middle">50 capsules</text>
    <text class="product-notice" x="189" y="349" text-anchor="middle">Dietary supplement</text>
    <text class="product-notice" x="189" y="371" text-anchor="middle">or professional use only</text>
  </g>
</svg>
</body>
</html>
```